National Training and assessment company needs a website

Create a 4 page website, simple but professional, the company provides training services to industry, resumes'/ CVs, personnel skill assessment, workplace skills profiling and develops manufactures and supplies training equipment for electrical/engineering training, Company title is Toren K Pty Ltd and also trades under BRW & Associates. letterheads etc all are done using dark green
Reason: Due to work commitments will be interstate from the 26/02 til 05/03/14
Target Market(s)
The market is broad covering the general public, secondary colleges and corporate sector
Industry/Entity Type
Training
Look and feel

```html
<!DOCTYPE html>
<html lang="en">
<head>
<meta charset="utf-8">
<title>Toren K Pty Ltd — Training &amp; Assessment</title>
<link rel="stylesheet" href="https://fonts.googleapis.com/css2?family=Roboto+Condensed:wght@300;400;700&family=Crimson+Text:ital,wght@1,600&display=swap">
<style>
  :root {
    --green: #0a7d0a;
    --green-soft: #9fd09f;
    --grey-text: #8a8a8a;
    --nav-text: #555;
    --line: #d6d6d6;
    --band: #efefef;
    --white: #fff;
  }
  * { margin: 0; padding: 0; box-sizing: border-box; }
  html, body { width: 1200px; height: 1000px; overflow: hidden; background: var(--white); }
  body { position: relative; font-family: "Roboto Condensed", Arial, sans-serif; color: var(--grey-text); }

  .top-bar { position: absolute; left: 0; top: 0; width: 1200px; height: 4px; background: var(--green); }

  .site-header { position: absolute; left: 0; top: 4px; width: 1200px; height: 148px; border-bottom: 1px solid var(--line); }
  .brand { position: absolute; left: 140px; top: 54px; color: var(--green); font-weight: 400; line-height: 1; }
  .brand__name { display: block; font-size: 46px; }
  .brand__sub { display: block; font-size: 33px; margin-top: 10px; }

  .phone { position: absolute; left: 622px; top: 19px; display: flex; align-items: center; gap: 4px;
           font-family: "Crimson Text", Georgia, serif; font-style: italic; font-size: 21px; color: #666; }
  .search { position: absolute; left: 776px; top: 14px; width: 337px; height: 31px; border: 1px solid #cfcfcf; background: var(--white); }
  .search__label { position: absolute; left: 136px; top: 6px; font-size: 15px; color: #b5b5b5; }
  .search__icon { position: absolute; right: 16px; top: 6px; }

  .main-nav { position: absolute; left: 640px; top: 108px; display: flex; height: 35px; }
  .main-nav a { display: block; height: 35px; line-height: 35px; font-size: 16px; font-weight: 700; color: var(--nav-text);
                text-decoration: none; text-transform: uppercase; }
  .main-nav .is-active { background: var(--green); color: var(--white); padding: 0 11px; margin-right: 17px; }
  .main-nav .nav-about { margin-right: 30px; }
  .main-nav .nav-services { margin-right: 27px; }
  .main-nav .nav-stories { margin-right: 27px; }

  .hero { position: absolute; left: 0; top: 152px; width: 1200px; height: 597px;
          background: radial-gradient(ellipse at 40% 50%, #ffffff 0%, #fbfbfb 60%, #f3f3f3 100%);
          border-bottom: 1px solid var(--line); }
  .hero__photo { position: absolute; left: 200px; top: 0; width: 390px; height: 586px;
                 background: linear-gradient(180deg, #f6f6f6 0%, #8a8a8a 35%, #5c5c5c 65%, #2a2a2a 100%); border-radius: 4px; }
  .hero__arrow { position: absolute; top: 312px; }
  .hero__arrow--prev { left: 134px; }
  .hero__arrow--next { left: 1068px; }
  .hero__title { position: absolute; left: 638px; top: 141px; font-size: 74px; line-height: 62px; font-weight: 400;
                 color: var(--green); letter-spacing: -1px; }
  .hero__text { position: absolute; left: 638px; top: 276px; width: 360px; font-size: 16px; line-height: 21px; font-weight: 300; }
  .hero__cta { position: absolute; left: 645px; top: 366px; width: 180px; height: 50px; background: var(--green); color: var(--white);
               font-family: "Crimson Text", Georgia, serif; font-style: italic; font-weight: 600; font-size: 29px;
               line-height: 50px; text-align: center; text-decoration: none; }

  .features { position: absolute; left: 0; top: 750px; width: 1200px; height: 250px; background: var(--band); }
  .feature { position: absolute; top: 0; }
  .feature__icon { position: absolute; top: 10px; }
  .feature__title { position: absolute; top: 73px; width: 240px; font-size: 29px; line-height: 32px; font-weight: 300;
                    color: var(--green); text-transform: uppercase; letter-spacing: -0.5px; }
  .feature__text { position: absolute; top: 166px; width: 190px; font-size: 16px; line-height: 21px; font-weight: 300; }
  .feature--help { left: 150px; }
  .feature--help .feature__icon { left: 34px; }
  .feature--company { left: 375px; }
  .feature--company .feature__icon { left: 78px; }
  .feature--company .feature__title { font-size: 26px; line-height: 27px; }
  .feature--company .feature__text { left: 4px; width: 210px; }
  .feature--training { left: 625px; }
  .feature--training .feature__icon { left: 43px; }
  .feature--signup { left: 850px; }
  .feature--signup .feature__icon { left: 46px; }
  .signup__input { position: absolute; left: 0; top: 169px; width: 267px; height: 31px; border: 1px solid #d0d0d0; background: var(--white);
                   font-size: 16px; font-weight: 300; color: #b0b0b0; padding: 5px 9px; }
  .signup__submit { position: absolute; left: 3px; top: 218px; width: 102px; height: 28px; background: var(--green); color: var(--white);
                    font-family: Arial, sans-serif; font-size: 13px; line-height: 28px; text-align: center; }
  .people-icon { width: 60px; height: 54px; border-radius: 50%; background: radial-gradient(circle at 50% 40%, #c9e7a0, #5fa83a); }
</style>
</head>
<body>
  <div class="top-bar"></div>

  <header class="site-header">
    <div class="brand">
      <span class="brand__name">Toren K Pty Ltd</span>
      <span class="brand__sub">BRW &amp; Associates</span>
    </div>

    <div class="phone">
      <svg width="20" height="20" viewBox="0 0 20 20" aria-hidden="true"><path d="M5 2c-2 1-3 3-2 6 2 5 6 9 11 10 2 0 3-1 3-2l-3-3-2 1c-2-1-4-3-5-5l1-2z" fill="#555"/></svg>
      <span>0400 152 608</span>
    </div>

    <div class="search">
      <span class="search__label">Search</span>
      <svg class="search__icon" width="18" height="18" viewBox="0 0 18 18" aria-hidden="true">
        <circle cx="7.5" cy="7.5" r="5.5" fill="none" stroke="#111" stroke-width="2"/>
        <line x1="11.5" y1="11.5" x2="16" y2="16" stroke="#111" stroke-width="2.4" stroke-linecap="round"/>
      </svg>
    </div>

    <nav class="main-nav">
      <a class="is-active" href="#">Home</a>
      <a class="nav-about" href="#">About Us</a>
      <a class="nav-services" href="#">Services</a>
      <a class="nav-stories" href="#">Success Stories</a>
      <a href="#">Contacts</a>
    </nav>
  </header>

  <section class="hero">
    <div class="hero__photo" role="img" aria-label="Photo of a young businessman in a grey suit sitting backwards on a folding chair"></div>
    <svg class="hero__arrow hero__arrow--prev" width="50" height="50" viewBox="0 0 50 50" aria-hidden="true">
      <circle cx="25" cy="25" r="22" fill="none" stroke="#e3e3e3" stroke-width="4"/>
      <path d="M30 15 L16 25 L30 35 Z" fill="#e3e3e3"/>
    </svg>
    <svg class="hero__arrow hero__arrow--next" width="50" height="50" viewBox="0 0 50 50" aria-hidden="true">
      <circle cx="25" cy="25" r="22" fill="none" stroke="#9fd09f" stroke-width="4"/>
      <path d="M20 15 L34 25 L20 35 Z" fill="#9fd09f"/>
    </svg>
    <h1 class="hero__title">DEVELOP YOUR<br>PERSONALITY</h1>
    <p class="hero__text">Praesent vestibulum molestie lacus. Aenean nonummy hendrerit mauris. Phasellus porta. Fusce suscipit varius.</p>
    <a class="hero__cta" href="#">Start Today!</a>
  </section>

  <section class="features">
    <div class="feature feature--help">
      <svg class="feature__icon" width="54" height="48" viewBox="0 0 54 48" aria-hidden="true">
        <ellipse cx="20" cy="17" rx="18" ry="14" fill="#f08a1c"/>
        <path d="M10 27 L6 36 L18 30 Z" fill="#f08a1c"/>
        <ellipse cx="34" cy="30" rx="17" ry="13" fill="#2a7fd0"/>
        <path d="M42 40 L48 46 L44 38 Z" fill="#2a7fd0"/>
      </svg>
      <h2 class="feature__title">How we can<br>help you?</h2>
      <p class="feature__text">Vestibulum molestie lacus. Aenean nonummy hendrerit mauris. Phasellus porta. Fusce suscipit varius mi.</p>
    </div>

    <div class="feature feature--company">
      <svg class="feature__icon" width="50" height="58" viewBox="0 0 50 58" aria-hidden="true">
        <g transform="rotate(30 25 29)">
          <rect x="17" y="4" width="16" height="36" rx="2" fill="#e9f3fb" stroke="#6f8fb0" stroke-width="2"/>
          <rect x="19" y="16" width="12" height="20" fill="#5fb3e8"/>
          <path d="M17 40 L25 54 L33 40 Z" fill="#d8d8d8" stroke="#6f8fb0" stroke-width="2"/>
        </g>
      </svg>
      <h2 class="feature__title">Company provides<br>training services<br>to industry</h2>
      <p class="feature__text">Praesent vestibulum molestie lacus. Aenean nonummy hendrerit mauris. Phasellus porta. Fusce suscipit varius.</p>
    </div>

    <div class="feature feature--training">
      <div class="feature__icon people-icon" role="img" aria-label="Icon of a small group of people"></div>
      <h2 class="feature__title">Best training<br>are here</h2>
      <p class="feature__text">Aenean nonummy hendrerit mauris. Phasellus porta. Fusce suscipit varius mi. Cum sociis natoque penatibus.</p>
    </div>

    <div class="feature feature--signup">
      <svg class="feature__icon" width="56" height="50" viewBox="0 0 56 50" aria-hidden="true">
        <g transform="rotate(-12 28 25)">
          <rect x="4" y="10" width="48" height="32" fill="#e8e8e8" stroke="#bdbdbd"/>
          <path d="M4 10 L28 26 L52 10" fill="none" stroke="#bdbdbd" stroke-width="1.5"/>
          <rect x="12" y="6" width="32" height="22" fill="#5fae3c"/>
          <text x="28" y="23" font-family="Arial, sans-serif" font-size="17" fill="#fff" text-anchor="middle">@</text>
        </g>
      </svg>
      <h2 class="feature__title">Sign up here</h2>
      <div class="signup__input">Enter your Email here</div>
      <div class="signup__submit">Submit</div>
    </div>
  </section>
</body>
</html>
```